Letterhead, business card and email signature design

I have a new company and I would like a professional letterhead, business card and email signature designed. Id like the business card to have room for a photo of the bearer. I'd also like the template to be editable so we can adapt for future members of staff etc.

```html
<!DOCTYPE html>
<html lang="en">
<head>
<meta charset="utf-8">
<title>Nimbus Relay – Stationery Set</title>
<link href="https://fonts.googleapis.com/css2?family=Lato:wght@400;700&display=swap" rel="stylesheet">
<style>
  :root {
    --navy: #1a3559;
    --magenta: #a61c5a;
    --white: #ffffff;
    --backdrop: #626262;
    --photo-light: #e6e2df;
    --photo-dark: #8a7a70;
  }
  * { margin: 0; padding: 0; box-sizing: border-box; }
  html, body { width: 1200px; height: 825px; overflow: hidden; }
  body {
    background: var(--backdrop);
    font-family: "Lato", sans-serif;
    position: relative;
  }
  .piece {
    position: absolute;
    background: var(--white);
    box-shadow: 10px 14px 22px rgba(0,0,0,0.35);
    overflow: hidden;
  }
  .piece > svg.wave { position: absolute; left: 0; top: 0; }

  .card-front { left: 160px; top: 87px; width: 342px; height: 196px; }
  .card-back  { left: 160px; top: 335px; width: 342px; height: 195px; }
  .email-signature { left: 80px; top: 586px; width: 502px; height: 152px; }
  .letterhead { left: 620px; top: 87px; width: 502px; height: 651px; }

  /* brand lockup */
  .brand { position: absolute; display: flex; align-items: center; }
  .brand-dot { border-radius: 50%; background: var(--navy); flex: none; }
  .brand-name {
    color: var(--navy);
    font-weight: 700;
    letter-spacing: 0.04em;
    white-space: nowrap;
    line-height: 1;
  }
  .card-front .brand { left: 25px; top: 39px; gap: 8px; }
  .card-front .brand-dot { width: 45px; height: 45px; }
  .card-front .brand-name { font-size: 10px; }

  .card-back .brand { left: 0; right: 0; top: 62px; gap: 11px; justify-content: center; }
  .card-back .brand-dot { width: 70px; height: 70px; }
  .card-back .brand-name { font-size: 14px; }

  .letterhead .brand { left: 30px; top: 30px; gap: 9px; }
  .letterhead .brand-dot { width: 67px; height: 67px; }
  .letterhead .brand-name { font-size: 14px; }

  .email-signature .brand { left: 35px; top: 26px; gap: 8px; }
  .email-signature .brand-dot { width: 53px; height: 53px; }
  .email-signature .brand-name { font-size: 11px; }

  /* photo */
  .bearer-photo {
    position: absolute; left: 234px; top: 20px;
    width: 94px; height: 94px; border-radius: 50%;
    border: 2px solid var(--magenta);
    background: radial-gradient(circle at 50% 40%, var(--photo-light) 0%, #c9bfb8 55%, var(--photo-dark) 100%);
  }

  /* identity */
  .bearer { position: absolute; color: var(--white); }
  .bearer-name { font-weight: 400; white-space: nowrap; line-height: 1.1; }
  .bearer-role { white-space: nowrap; line-height: 1.2; }
  .card-front .bearer { left: 25px; top: 146px; }
  .card-front .bearer-name { color: var(--magenta); font-size: 15px; }
  .card-front .bearer-role { font-size: 8.5px; margin-top: 3px; }

  .email-signature .bearer { right: 14px; top: 74px; text-align: right; }
  .email-signature .bearer-name { font-size: 13px; letter-spacing: 0.03em; }
  .email-signature .bearer-role { color: var(--magenta); font-size: 8.5px; letter-spacing: 0.04em; }

  /* contacts */
  .contacts { position: absolute; list-style: none; color: var(--white); text-align: right; }
  .contacts li { display: flex; justify-content: flex-end; align-items: center; gap: 6px; white-space: nowrap; }
  .contacts svg { flex: none; }
  .card-front .contacts { right: 15px; top: 134px; font-size: 8.5px; }
  .card-front .contacts li { height: 15.3px; }
  .email-signature .contacts { right: 14px; top: 104px; font-size: 9.3px; letter-spacing: 0.02em; }
  .email-signature .contacts li { height: 12px; }
  .letterhead .contacts { right: 29px; top: 585px; font-size: 7.8px; }
  .letterhead .contacts li { height: 12.3px; }

  .web-address {
    position: absolute; left: 0; right: 0; top: 164px;
    text-align: center; font-size: 9px; letter-spacing: 0.06em; color: var(--navy);
  }
  .web-address .domain { color: var(--magenta); }
</style>
</head>
<body>

<svg width="0" height="0" style="position:absolute">
  <defs>
    <symbol id="icon-phone" viewBox="0 0 8 10"><rect x="1.5" y="0.5" width="5" height="9" rx="1" fill="none" stroke="#a61c5a" stroke-width="1"/></symbol>
    <symbol id="icon-mail" viewBox="0 0 10 8"><rect x="0.5" y="1" width="9" height="6" fill="#a61c5a"/><path d="M0.5 1 L5 4.5 L9.5 1" fill="none" stroke="#1a3559" stroke-width="0.8"/></symbol>
    <symbol id="icon-web" viewBox="0 0 10 10"><circle cx="5" cy="5" r="4.3" fill="#a61c5a"/><path d="M0.7 5 H9.3 M5 0.7 C2.5 3 2.5 7 5 9.3 M5 0.7 C7.5 3 7.5 7 5 9.3" fill="none" stroke="#1a3559" stroke-width="0.6"/></symbol>
  </defs>
</svg>

<!-- Business card front -->
<section class="piece card-front">
  <svg class="wave" width="342" height="196" viewBox="0 0 342 196">
    <path d="M0 78 C40 122 110 128 180 100 C240 74 290 56 342 72 L342 196 L0 196 Z" fill="var(--magenta)"/>
    <path d="M0 86 C40 128 110 134 180 108 C240 82 290 64 342 80 L342 196 L0 196 Z" fill="var(--white)"/>
    <path d="M0 90 C40 132 110 138 180 112 C240 86 290 68 342 84 L342 196 L0 196 Z" fill="var(--navy)"/>
  </svg>
  <div class="brand"><span class="brand-dot"></span><span class="brand-name">NIMBUS RELAY</span></div>
  <div class="bearer-photo" role="img" aria-label="Portrait photo of the card bearer"></div>
  <div class="bearer">
    <p class="bearer-name">Daniel Harper</p>
    <p class="bearer-role">Founder &amp; CEO</p>
  </div>
  <ul class="contacts">
    <li>000 000 0000 <svg width="8" height="10"><use href="#icon-phone"/></svg></li>
    <li>d_harper@nimbusrelay.com <svg width="9" height="8"><use href="#icon-mail"/></svg></li>
    <li>www.nimbusrelay.com <svg width="9" height="9"><use href="#icon-web"/></svg></li>
  </ul>
</section>

<!-- Business card back -->
<section class="piece card-back">
  <div class="brand"><span class="brand-dot"></span><span class="brand-name">NIMBUS RELAY</span></div>
  <p class="web-address">www.<span class="domain">nimbusrelay</span>.com</p>
</section>

<!-- Email signature -->
<section class="piece email-signature">
  <svg class="wave" width="502" height="152" viewBox="0 0 502 152">
    <path d="M0 52 C30 100 80 118 150 112 C240 104 300 50 380 28 C430 14 475 18 502 34 L502 152 L0 152 Z" fill="var(--magenta)"/>
    <path d="M0 68 C30 112 80 128 150 122 C240 114 300 62 380 42 C430 30 475 34 502 50 L502 152 L0 152 Z" fill="var(--white)"/>
    <path d="M0 76 C30 118 80 134 150 128 C240 120 300 70 380 50 C430 38 475 42 502 58 L502 152 L0 152 Z" fill="var(--navy)"/>
  </svg>
  <div class="brand"><span class="brand-dot"></span><span class="brand-name">NIMBUS RELAY</span></div>
  <div class="bearer">
    <p class="bearer-name">Daniel Harper</p>
    <p class="bearer-role">Founder &amp; CEO</p>
  </div>
  <ul class="contacts">
    <li>000 000 0000 <svg width="8" height="10"><use href="#icon-phone"/></svg></li>
    <li>d_harper@nimbusrelay.com <svg width="9" height="8"><use href="#icon-mail"/></svg></li>
    <li>www.nimbusrelay.com <svg width="9" height="9"><use href="#icon-web"/></svg></li>
  </ul>
</section>

<!-- Letterhead -->
<section class="piece letterhead">
  <svg class="wave" width="502" height="651" viewBox="0 0 502 651">
    <path d="M0 540 C20 600 70 640 150 630 C240 618 320 560 390 538 C440 522 480 528 502 550 L502 651 L0 651 Z" fill="var(--magenta)"/>
    <path d="M0 558 C22 612 72 648 150 640 C240 630 320 574 390 552 C440 538 480 544 502 566 L502 651 L0 651 Z" fill="var(--white)"/>
    <path d="M0 566 C22 618 72 652 150 646 C240 638 320 582 390 560 C440 546 480 552 502 574 L502 651 L0 651 Z" fill="var(--navy)"/>
  </svg>
  <div class="brand"><span class="brand-dot"></span><span class="brand-name">NIMBUS RELAY</span></div>
  <ul class="contacts">
    <li>000 000 0000 <svg width="7" height="9"><use href="#icon-phone"/></svg></li>
    <li>d_harper@nimbusrelay.com <svg width="8" height="7"><use href="#icon-mail"/></svg></li>
    <li>www.nimbusrelay.com <svg width="8" height="8"><use href="#icon-web"/></svg></li>
  </ul>
</section>

</body>
</html>
```